bramblecrest paving card makeover

were a excavation/paving contractor from Monterey ca, I'm looking to have a card designed front and back that has company details on the front and a list of the services we offer on the back.

Target Market(s)

home owners property management companies

Industry/Entity Type

Contractor

Contact Information for Business Card

bramblecrest paving 418 larkmoor st Monterey ca. licensed, insured and bonded
lic#657920 gerald pinsky operations manager

Font styles to use
Serif
Sans Serif

Colors
f78f20

Requirements
Must have
• a list of my services on back, asphalt construction and maintenance, drainage, foundations, retaining walls, chip seals, excavation, grading, landscape ground work, interlocking paver, hydro-seeding, structured and driveway demolition, utility trenching and stump removal.
Nice to have
• my new domain and page address I'm acquiring from pixel bazaar.

```html
<!DOCTYPE html>
<html lang="en">
<head>
<meta charset="utf-8">
<title>Bramblecrest Paving – Business Card</title>
<link href="https://fonts.googleapis.com/css2?family=Lato:wght@400;700&display=swap" rel="stylesheet">
<style>
  :root {
    --backdrop: #555555;
    --card-light: #ffffff;
    --card-dark: #000000;
    --ink-dark: #111111;
    --ink-light: #ffffff;
  }
  * { margin: 0; padding: 0; box-sizing: border-box; }
  html, body { width: 1200px; height: 900px; overflow: hidden; }
  body {
    background: var(--backdrop);
    font-family: "Lato", Arial, sans-serif;
    position: relative;
  }
  .card {
    position: absolute;
    top: 170px;
    width: 347px;
    height: 561px;
    box-shadow: 3px 4px 8px rgba(0,0,0,0.45);
    text-align: center;
  }
  .card-front { left: 259px; background: var(--card-light); color: var(--ink-dark); }
  .card-back { left: 631px; background: var(--card-dark); color: var(--ink-light); }

  .brand-mark {
    position: absolute;
    left: 0; right: 0;
    top: 140px;
    display: flex;
    flex-direction: column;
    align-items: center;
    gap: 12px;
  }
  .brand-dot {
    width: 26px; height: 26px;
    border-radius: 50%;
    background: currentColor;
  }
  .brand-name {
    font-size: 22px;
    font-weight: 700;
    letter-spacing: 2px;
    line-height: 1.2;
  }

  .contact { position: absolute; left: 0; right: 0; top: 318px; }
  .person-name { font-size: 20px; font-weight: 700; letter-spacing: 0.5px; line-height: 24px; }
  .person-title { font-size: 15px; line-height: 18px; }
  .licence { font-size: 15px; margin-top: 11px; line-height: 18px; }
  .icon-rule {
    display: flex; align-items: center; justify-content: center;
    margin: 10px auto 4px; width: 187px; gap: 3px;
  }
  .icon-rule .rule { flex: 1; height: 1px; background: var(--ink-dark); }
  .icon-rule svg { display: block; }
  .contact-lines { font-size: 15px; line-height: 20.5px; }
  .divider { width: 187px; height: 1px; background: var(--ink-dark); margin: 5px auto 5px; }
  .company { font-size: 14px; letter-spacing: 0.3px; line-height: 18px; }
  .address { font-size: 16px; line-height: 22px; }

  .services { position: absolute; left: 0; right: 0; top: 308px; }
  .services-heading {
    display: flex; align-items: center; justify-content: center;
    font-size: 15.5px; letter-spacing: 0.3px; gap: 4px;
    margin: 0 32px;
  }
  .services-heading .rule { flex: 1; height: 1px; background: var(--ink-light); }
  .services-list { list-style: none; margin-top: 16px; font-size: 16px; line-height: 23.4px; }
  .sep {
    display: inline-block; width: 7px; height: 7px; border-radius: 50%;
    background: var(--ink-light); margin: 0 8px; vertical-align: middle;
  }
</style>
</head>
<body>
  <section class="card card-front">
    <div class="brand-mark">
      <span class="brand-dot"></span>
      <span class="brand-name">BRAMBLECREST<br>PAVING</span>
    </div>
    <div class="contact">
      <p class="person-name">GERALD PINSKY</p>
      <p class="person-title">Managing Director</p>
      <p class="licence">Lic# 657920</p>
      <div class="icon-rule">
        <span class="rule"></span>
        <svg width="20" height="20" viewBox="0 0 20 20" aria-label="Phone"><circle cx="10" cy="10" r="10" fill="#111"/><path d="M6 7.5c0-1 1-1.5 1.6-1.5l1 2-.8.8c.5 1 1.3 1.8 2.3 2.3l.8-.8 2 1c0 .6-.5 1.6-1.5 1.6C8.6 13 6 10.4 6 7.5z" fill="#fff"/></svg>
        <svg width="20" height="20" viewBox="0 0 20 20" aria-label="Email"><circle cx="10" cy="10" r="10" fill="#111"/><rect x="5.5" y="6.8" width="9" height="6.4" fill="#fff"/><path d="M5.5 6.8l4.5 3.6 4.5-3.6" fill="none" stroke="#111" stroke-width="1"/></svg>
        <svg width="20" height="20" viewBox="0 0 20 20" aria-label="Website"><circle cx="10" cy="10" r="10" fill="#111"/><circle cx="10" cy="10" r="4.6" fill="none" stroke="#fff" stroke-width="1.2"/><path d="M5.4 10h9.2M10 5.4c-2 2.6-2 6.6 0 9.2M10 5.4c2 2.6 2 6.6 0 9.2" fill="none" stroke="#fff" stroke-width="1"/></svg>
        <span class="rule"></span>
      </div>
      <div class="contact-lines">
        <p>444 555 7219</p>
        <p>info@youremail.com</p>
        <p>www.websitename.com</p>
      </div>
      <div class="divider"></div>
      <p class="company">BRAMBLECREST PAVING</p>
      <p class="address">418 larkmoor st Monterey ca.</p>
    </div>
  </section>

  <section class="card card-back">
    <div class="brand-mark">
      <span class="brand-dot"></span>
      <span class="brand-name">BRAMBLECREST<br>PAVING</span>
    </div>
    <div class="services">
      <h2 class="services-heading"><span class="rule"></span><span style="font-weight:400">SERVICES WE OFFER</span><span class="rule"></span></h2>
      <ul class="services-list">
        <li>Asphalt construction and maintenance</li>
        <li>Drainage<span class="sep"></span>Foundations</li>
        <li>Retaining walls<span class="sep"></span>Chip seals</li>
        <li>Excavation<span class="sep"></span>Grading</li>
        <li>Landscape ground work</li>
        <li>Interlocking paver<span class="sep"></span>Hydro-seeding</li>
        <li>Structured and driveway demolition</li>
        <li>Utility trenching and stump removal</li>
      </ul>
    </div>
  </section>
</body>
</html>
```